Business Card Design

We need a business card designed to portray the message that we are wedding and event stylists. We set up garden ceremonies and style wedding reception venues with chair covers and sashes, backdrops and draping's, wishing wells, tealight holders, table centerpieces. We also style corporate functions - Christmas parties, gala dinners, school formals, award nights. The colour of our uniforms are black and hot pink, if these colours could be incorporated. We would like to be able to use this design for letterhead, flyers and postcards etc. We would like the design to portray a professional, classic image that would relate to both spectrums of our business, weddings and corporate events. If you could develop a logo to incorporate would be great

Target Market(s)

brides, corporate compaines

Industry/Entity Type

Wedding

Contact Information for Business Card

Velvet Crest Occasions & Party Hire
Phone: 0417 553 916 Email:vcoph@fernmail.example
Web: www.velvetcrestoccasions.example.au

Requirements
Must have
• Must include that we set up for weddings, engagements, birthdays, anniversaries, corporate functions, school formals, any occasion.

```html
<!DOCTYPE html>
<html lang="en">
<head>
<meta charset="utf-8">
<title>Velvet Crest Occasions &amp; Party Hire — Business Card</title>
<link rel="stylesheet" href="https://fonts.googleapis.com/css2?family=Pinyon+Script&family=Questrial&display=swap">
<style>
  :root {
    --page-bg: #2a2a2c;
    --card-white: #f7f6f7;
    --card-shade: #e6e4e7;
    --ink-black: #1c1c1c;
    --hot-pink: #b8288f;
    --icon-grey: #6b6b6d;
    --dove-tone: #ececf0;
    --gem-tone: #d4d4d8;
    --sparkle-tone: #e9e7eb;
  }
  * { margin: 0; padding: 0; box-sizing: border-box; }
  html, body {
    width: 1200px; height: 900px; overflow: hidden;
    background: var(--page-bg);
  }
  .business-card {
    position: absolute;
    left: 100px; top: 164px;
    width: 1000px; height: 572px;
    background:
      radial-gradient(ellipse at 55% 40%, var(--card-white) 0%, var(--card-white) 35%, var(--card-shade) 100%);
    box-shadow: 0 20px 50px rgba(0,0,0,0.55);
    overflow: hidden;
  }
  .sparkle-backdrop {
    position: absolute;
    left: 0; top: 0;
    width: 1000px; height: 572px;
    background: radial-gradient(ellipse at 50% 40%, rgba(255,255,255,0) 0%, rgba(255,255,255,0) 30%, var(--sparkle-tone) 75%, rgba(233,231,235,0) 100%);
    opacity: 0.6;
  }
  .brand-name {
    position: absolute;
    left: 82px; top: 96px;
    font-family: "Pinyon Script", cursive;
    font-weight: 400;
    font-size: 56px;
    color: var(--ink-black);
    line-height: 1;
    white-space: nowrap;
  }
  .service-list {
    position: absolute;
    left: 92px; top: 178px;
    font-family: "Questrial", sans-serif;
    font-size: 21px;
    letter-spacing: 2.4px;
    line-height: 1.25;
    color: var(--hot-pink);
  }
  .contact-list {
    position: absolute;
    left: 80px; top: 378px;
    list-style: none;
    font-family: "Questrial", sans-serif;
    color: var(--hot-pink);
  }
  .contact-item {
    display: flex; align-items: center;
    gap: 22px;
    height: 48px;
  }
  .contact-item svg { width: 34px; height: 34px; flex: none; }
  .contact-phone { font-size: 34px; letter-spacing: 4px; }
  .contact-email { font-size: 30px; letter-spacing: 3.5px; }
  .contact-web { font-size: 22px; letter-spacing: 4.5px; }
  .dove-art {
    position: absolute;
    right: 30px; top: 14px;
    width: 110px; height: 76px;
    border-radius: 50%;
    background: radial-gradient(ellipse, var(--dove-tone) 0%, rgba(236,236,240,0) 70%);
  }
  .gem-art {
    position: absolute;
    right: 38px; top: 250px;
    width: 70px; height: 58px;
    border-radius: 8px;
    background: linear-gradient(135deg, var(--card-white), var(--gem-tone));
  }
</style>
</head>
<body>
  <main class="business-card">
    <div class="sparkle-backdrop" role="img" aria-label="Soft radial sparkle pattern behind the card text"></div>

    <h1 class="brand-name">Velvet Crest Occasions &amp; Party Hire</h1>
    <p class="service-list">-weddings, engagements, birthdays, anniversaries,<br>corporate functions, school formals, any occasion-</p>

    <ul class="contact-list">
      <li class="contact-item contact-phone">
        <svg viewBox="0 0 34 34" aria-hidden="true">
          <path d="M6 8c3-3 6-3 7 0l2 4c1 2-1 3-2 4 1 3 3 5 6 6 1-1 2-3 4-2l4 2c3 1 3 4 0 7-7 4-25-14-21-21z" fill="var(--icon-grey)"/>
        </svg>
        <span>0417 553 916</span>
      </li>
      <li class="contact-item contact-email">
        <svg viewBox="0 0 34 34" aria-hidden="true">
          <rect x="3" y="8" width="28" height="19" rx="2" fill="var(--icon-grey)"/>
          <path d="M4 9l13 10 13-10" fill="none" stroke="#f0f0f0" stroke-width="2"/>
        </svg>
        <span>vcoph@fernmail.example</span>
      </li>
      <li class="contact-item contact-web">
        <svg viewBox="0 0 34 34" aria-hidden="true">
          <circle cx="17" cy="17" r="14" fill="var(--icon-grey)"/>
          <g fill="none" stroke="#f0f0f0" stroke-width="1.5">
            <ellipse cx="17" cy="17" rx="6" ry="14"/>
            <line x1="3" y1="17" x2="31" y2="17"/>
            <line x1="17" y1="3" x2="17" y2="31"/>
            <path d="M6 10h22M6 24h22"/>
          </g>
        </svg>
        <span>www.velvetcrestoccasions.example.au</span>
      </li>
    </ul>

    <div class="dove-art" role="img" aria-label="White dove in flight"></div>
    <div class="gem-art" role="img" aria-label="Sparkling cut diamond"></div>
  </main>
</body>
</html>
```